People Analytics Company needs Web Design and CSS

We need a refreshed design for a People Analytics company called Vontiq Systems Inc. We have developed an online survey tool that our immediate need is to make it look snazzier for upcoming pilots with prospective companies. Dark Blue and Orange are the colors we like to use but the survey should be "neutral" - we don't want to influence any responses based on colors.

Target Market(s)

Enterprise Users

Industry/Entity Type

It Company

Coding

Coded - Design and coding required

Number of Pages Required

3 page

Font styles to use
Sans Serif

Colors
0556a4
f37122

Requirements
Must have
• User friendly way of responding to survey questions that is suitable for a tablet (fat fingers). Drag and Drop is also very hard on tablet.
• Neutral look and feel to reduce any potential respondent bias.
• Colors consistent with brand colors attached in document.
• Minimal scrolling is best.
Should not have
• Too many colors.

```html
<!DOCTYPE html>
<html lang="en">
<head>
<meta charset="utf-8">
<title>Vontiq Systems Inc. – Step 2</title>
<link rel="stylesheet" href="https://fonts.googleapis.com/css2?family=Montserrat:wght@400;500;700&family=Roboto:wght@300;400&display=swap">
<style>
  :root {
    --brand-blue: #0556a4;
    --brand-blue-dark: #05468a;
    --brand-orange: #f37122;
    --brand-orange-dark: #d95f17;
    --navy: #0d1b3e;
    --panel-grey: #e4e7ea;
    --card-white: #ffffff;
    --text-body: #555a60;
    --text-number: #4a4f55;
    --header-line: #d4d6d9;
    --footer-bg: #1d2023;
    --footer-text: #e6e8ea;
  }
  * { box-sizing: border-box; margin: 0; padding: 0; }
  html, body { width: 1200px; height: 972px; overflow: hidden; background: #fff; }
  body { position: relative; font-family: "Roboto", Arial, sans-serif; }

  .site-header {
    position: absolute; left: 0; top: 0; width: 1200px; height: 96px;
    border-bottom: 1px solid var(--header-line);
    box-shadow: 0 1px 2px rgba(0,0,0,0.06);
  }
  .brand {
    position: absolute; left: 107px; top: 29px;
    display: flex; align-items: center; gap: 10px;
    font-family: "Montserrat", Arial, sans-serif; font-weight: 700;
    font-size: 22px; color: var(--navy);
  }
  .brand-mark { width: 36px; height: 36px; background: var(--navy); border-radius: 3px; }
  .header-actions { position: absolute; top: 27px; right: 74px; display: flex; gap: 11px; }
  .btn {
    height: 42px; display: flex; align-items: center; justify-content: center;
    font-family: "Montserrat", Arial, sans-serif; font-size: 11px; font-weight: 500;
    color: #fff; border-radius: 3px; text-transform: uppercase; letter-spacing: 0.2px;
  }
  .btn-signin { width: 105px; background: linear-gradient(var(--brand-blue), var(--brand-blue-dark)); }
  .btn-start { width: 121px; background: linear-gradient(var(--brand-orange), var(--brand-orange-dark)); }

  .step-title {
    position: absolute; left: 111px; top: 127px;
    font-family: "Montserrat", Arial, sans-serif; font-weight: 400;
    font-size: 27px; color: var(--brand-orange);
  }

  .choice-panel {
    position: absolute; left: 111px; top: 192px; width: 727px; height: 639px;
    background: var(--panel-grey);
    padding: 24px 24px 0 25px;
    display: grid; grid-template-columns: 327px 327px; column-gap: 24px; row-gap: 16px;
    grid-auto-rows: 104px;
  }
  .choice-card {
    background: var(--card-white);
    box-shadow: 0 1px 2px rgba(0,0,0,0.12);
    display: flex; align-items: center; justify-content: center;
    padding: 0 26px; text-align: center;
    font-size: 12px; line-height: 24px; color: var(--text-body);
  }

  .rank-list {
    position: absolute; left: 870px; top: 193px;
    display: flex; flex-direction: column; gap: 13px;
  }
  .rank-row { display: flex; align-items: center; height: 81px; }
  .rank-number { width: 29px; font-size: 24px; font-weight: 300; color: var(--text-number); padding-left: 6px; }
  .rank-slot {
    width: 189px; height: 81px; background: var(--brand-blue);
    display: flex; align-items: center; justify-content: center; gap: 8px;
    color: #fff; font-size: 25px; font-weight: 400;
  }
  .rank-note { font-size: 12px; padding-top: 5px; }

  .site-footer {
    position: absolute; left: 0; top: 891px; width: 1200px; height: 81px;
    background: var(--footer-bg); color: var(--footer-text); font-size: 11px;
  }
  .footer-links { position: absolute; left: 111px; top: 31px; }
  .footer-links span { margin: 0 4px; }
  .copyright { position: absolute; right: 111px; top: 31px; }
</style>
</head>
<body>
  <header class="site-header">
    <div class="brand"><span class="brand-mark"></span>Vontiq Systems Inc.</div>
    <nav class="header-actions">
      <a class="btn btn-signin">Sign In</a>
      <a class="btn btn-start">Get Started</a>
    </nav>
  </header>

  <h1 class="step-title">Step 2 : Prioritizing the previous choice</h1>

  <section class="choice-panel">
    <div class="choice-card">Lorem ipsum dolor sit amet, consectetuer adipiscing elit, sed diam nonummy nibh euismod tincidunt ut laoreet dolore.</div>
    <div class="choice-card">Ut wisi enim ad minim veniam, quis nostrud exerci tation ullamcorper suscipit lobortis nisl ut aliquip ex ea commodo consequat</div>
    <div class="choice-card">Duis autem vel eum iriure dolor in hendrerit in vulputate velit esse molestie consequat, vel illum dolore eu feugiat nulla facilisis</div>
    <div class="choice-card">Nam liber tempor cum soluta nobis eleifend option congue nihil imperdiet doming id quod mazim placerat facer possim assum.</div>
    <div class="choice-card">Mirum est notare quam littera gothica, quam nunc putamus parum claram, anteposuerit litterarum formas humanitatis per seacula.</div>
    <div class="choice-card">Ut wisi enim ad minim veniam, quis nostrud exerci tation ullamcorper suscipit lobortis nisl ut aliquip ex ea commodo consequat</div>
    <div class="choice-card">Lorem ipsum dolor sit amet, consectetuer adipiscing elit, sed diam nonummy nibh euismod tincidunt ut laoreet dolore.</div>
    <div class="choice-card">Lorem ipsum dolor sit amet, consectetuer adipiscing elit, sed diam nonummy nibh euismod tincidunt ut laoreet dolore.</div>
    <div class="choice-card">Duis autem vel eum iriure dolor in hendrerit in vulputate velit esse molestie consequat, vel illum dolore eu feugiat nulla facilisis</div>
    <div class="choice-card">Nam liber tempor cum soluta nobis eleifend option congue nihil imperdiet doming id quod mazim placerat facer possim assum.</div>
  </section>

  <ol class="rank-list">
    <li class="rank-row"><span class="rank-number">1</span><div class="rank-slot"># 1</div></li>
    <li class="rank-row"><span class="rank-number">2</span><div class="rank-slot"># 2</div></li>
    <li class="rank-row"><span class="rank-number">3</span><div class="rank-slot"># 3</div></li>
    <li class="rank-row"><span class="rank-number">4</span><div class="rank-slot"># 4</div></li>
    <li class="rank-row"><span class="rank-number">5</span><div class="rank-slot"># 5</div></li>
    <li class="rank-row"><span class="rank-number">6</span><div class="rank-slot"># 6</div></li>
    <li class="rank-row"><span class="rank-number">7</span><div class="rank-slot"># 7 <span class="rank-note">Latest Important</span></div></li>
  </ol>

  <footer class="site-footer">
    <div class="footer-links">Terms Of Service<span>|</span>Privacy Policy<span>|</span>Contact Us</div>
    <div class="copyright">@ 2015 Vontiq.All Right Reserved.</div>
  </footer>
</body>
</html>
```